Harbourline Homes Business Card Design

We need a business card for an established builder of high quality bespoke homes in Auckland and Northland. We build and renovate homes collaboratively facilitating effective communication between owners, builders, architects, suppliers and tradespeople. We have never built or renovated a home that leaks or has faults. We only use reliable materials. We have never been sued or had legal action taken against us. We are honest builders of bespoke homes not group mass produced homes. Our niche market is in character homes. We practice sustainability and have built a lot of coastal property. We have been in business for over thirty years . We would like to see natural colors of the environment sand,sea and maybe vegetation . The design should communicate quality, sustainability,fair pricing, open communication and the originality of bespoke building. And the fact that the builder is registered.

Business

Rowan Tillery Builders
Ph. 027318592
18 Garnet Rd Ferndale Bay Auckland 0814
PO Box 958 Mangawhai 0371

```html
<!DOCTYPE html>
<html lang="en">
<head>
<meta charset="utf-8">
<title>Harbourline Homes – Business Card</title>
<link href="https://fonts.googleapis.com/css2?family=Open+Sans:wght@400;800&display=swap" rel="stylesheet">
<style>
  :root {
    --backdrop: #4a3f3a;
    --card: #1b1b1c;
    --card-edge: #262627;
    --brand-red: #c4161c;
    --text-light: #e6e6e6;
    --logo-grey: #c9c9c9;
  }
  * { box-sizing: border-box; margin: 0; padding: 0; }
  html, body {
    width: 1200px; height: 844px; overflow: hidden;
    background: var(--backdrop);
    font-family: "Open Sans", Arial, sans-serif;
  }
  .stage {
    position: relative; width: 1200px; height: 844px;
    display: flex; align-items: center; justify-content: center; gap: 60px;
  }
  .card {
    position: relative; width: 520px; height: 300px;
    background: var(--card);
    border: 1px solid var(--card-edge);
    box-shadow: 0 10px 30px rgba(0,0,0,.45);
  }
  .brand {
    display: flex; align-items: center; gap: 10px;
    font-weight: 800; color: var(--logo-grey);
    letter-spacing: -0.5px; white-space: nowrap;
  }
  .brand-mark {
    width: 14px; height: 14px; background: var(--brand-red); flex: none;
  }
  .card-back {
    display: flex; justify-content: space-between; align-items: center;
    padding: 0 28px;
  }
  .card-back .brand {
    font-size: 22px; margin-top: 70px;
  }
  .card-front .brand {
    position: absolute; left: 50%; top: 50%;
    transform: translate(-50%, -50%); font-size: 42px;
  }
  .card-front .brand-mark { width: 16px; height: 16px; }
  .contact {
    text-align: right; color: var(--text-light);
    font-size: 13px; line-height: 1.55; font-style: normal;
  }
  .contact-name {
    color: var(--brand-red); font-size: 15px; margin-bottom: 2px;
  }
  .contact-phone {
    display: flex; justify-content: flex-end; align-items: center; gap: 8px;
    margin-bottom: 12px;
  }
  .contact-phone svg { width: 11px; height: 11px; fill: var(--brand-red); }
</style>
</head>
<body>
<main class="stage">
  <section class="card card-back">
    <div class="brand"><span class="brand-mark"></span>Harbourline Homes</div>
    <address class="contact">
      <p class="contact-name">Rowan Tillery Builders</p>
      <p class="contact-phone">027318592
        <svg viewBox="0 0 24 24" aria-hidden="true"><path d="M6.6 10.8a15.1 15.1 0 0 0 6.6 6.6l2.2-2.2a1 1 0 0 1 1-.25 11.4 11.4 0 0 0 3.6.57 1 1 0 0 1 1 1V20a1 1 0 0 1-1 1A17 17 0 0 1 3 4a1 1 0 0 1 1-1h3.5a1 1 0 0 1 1 1c0 1.25.2 2.45.57 3.57a1 1 0 0 1-.25 1z"/></svg>
      </p>
      <p>18 Garnet Rd Ferndale</p>
      <p>Bay Auckland 0814</p>
      <p>PO Box 958 Mangawhai 0371</p>
    </address>
  </section>
  <section class="card card-front">
    <div class="brand"><span class="brand-mark"></span>Harbourline Homes</div>
  </section>
</main>
</body>
</html>
```